Create a professional, eye-catching business card design that reflects the values and services of Brookfern Veterinary Hospital. we provide veterinary services and the business card should be a memorable representation of the clinic and align with its branding and mission. our tag line is "Life Long Companions, Lifelong Care"
Use clean, modern typography. Prioritize readability and professionalism. We would like to see designs that use the color blue, as in the logo example. the final design should communicate professionalism and care, with attention to detail.

```html
<!DOCTYPE html>
<html lang="en">
<head>
<meta charset="utf-8">
<title>Brookfern Veterinary Hospital – Business Cards</title>
<link href="https://fonts.googleapis.com/css2?family=Open+Sans:wght@400;600;700;800&display=swap" rel="stylesheet">
<style>
  :root {
    --bg: #3a3b3d;
    --navy-deep: #0e1a45;
    --navy: #1a2c68;
    --navy-soft: #2a3d7c;
    --navy-line: rgba(120, 145, 210, 0.35);
    --gold: #e3a82b;
    --white: #ffffff;
    --text-soft: #e6eaf5;
  }
  * { box-sizing: border-box; margin: 0; padding: 0; }
  html, body {
    width: 1200px; height: 900px; overflow: hidden;
    background: var(--bg);
    font-family: "Open Sans", Arial, sans-serif;
  }
  .canvas { position: relative; width: 1200px; height: 900px; }

  .card {
    position: absolute;
    width: 640px; height: 366px;
    border-radius: 0 34px 0 34px;
    overflow: hidden;
    background: linear-gradient(200deg, var(--navy) 0%, var(--navy-deep) 100%);
    box-shadow: 0 18px 40px rgba(0,0,0,0.45);
    color: var(--white);
  }
  .card--front { left: 100px; top: 60px; }
  .card--back  { left: 460px; top: 474px; }

  .decor-arc {
    position: absolute;
    border-radius: 50%;
  }
  .card--front .decor-arc {
    left: -150px; top: 40px; width: 520px; height: 520px;
    background: radial-gradient(circle at 40% 40%, var(--navy-soft), var(--navy-deep) 70%);
    box-shadow: inset -6px -4px 10px rgba(0,0,0,0.35), 3px 2px 4px rgba(110,130,200,0.25);
  }
  .card--back .decor-arc {
    left: -120px; top: 50px; width: 480px; height: 480px;
    border: 2px solid var(--navy-line);
    background: radial-gradient(circle at 40% 60%, rgba(70,95,170,0.35), rgba(40,60,130,0.05) 70%);
  }

  .brand {
    position: absolute;
    display: flex; align-items: center; gap: 12px;
  }
  .brand__dot {
    width: 22px; height: 22px; border-radius: 50%;
    background: var(--white);
    flex: none;
  }
  .brand__name {
    font-weight: 700; color: var(--white);
    line-height: 1.05; text-transform: uppercase;
  }
  .brand__name span { display: block; }
  .brand__name .main { font-size: 36px; letter-spacing: 1px; }
  .brand__name .sub { font-size: 13.5px; letter-spacing: 1.2px; }

  .card--front .brand { right: 44px; top: 78px; }
  .card--back .brand { right: 40px; top: 150px; }

  .front-tagline {
    position: absolute; right: 44px; top: 176px;
    width: 250px;
    border-top: 1.5px solid var(--gold);
    padding-top: 8px;
    text-align: center;
    font-weight: 600; font-size: 17px; line-height: 1.25;
  }

  .contact {
    position: absolute; left: 40px; top: 40px;
    font-size: 14.5px; color: var(--text-soft); line-height: 1.45;
  }
  .contact__title {
    color: var(--gold); font-weight: 700; font-size: 16px; letter-spacing: 0.3px;
  }
  .contact__sub { margin-left: 14px; }
  .contact__address { margin: 12px 0 0 28px; }
  .contact__list { list-style: none; margin: 6px 0 0 28px; }
  .contact__list li { display: flex; align-items: center; gap: 10px; }
  .contact__list svg { width: 16px; height: 16px; flex: none; }

  .back-rule {
    position: absolute; left: 40px; top: 272px;
    width: 330px; height: 0;
    border-top: 1.5px solid var(--gold);
  }
  .back-tagline {
    position: absolute; left: 40px; top: 284px;
    font-weight: 700; font-size: 19px; color: var(--white);
  }
</style>
</head>
<body>
<main class="canvas">

  <section class="card card--front" aria-label="Business card front">
    <div class="decor-arc" role="img" aria-label="Embossed circular backdrop"></div>
    <div class="brand">
      <span class="brand__dot"></span>
      <p class="brand__name"><span class="main">Brookfern</span><span class="sub">Veterinary Hospital</span></p>
    </div>
    <p class="front-tagline">Life Long Companions<br>Lifelong Care</p>
  </section>

  <section class="card card--back" aria-label="Business card back">
    <div class="decor-arc" role="img" aria-label="Faint circular backdrop"></div>
    <div class="contact">
      <p class="contact__title">BROOKFERN FAMILY</p>
      <p class="contact__sub">Owned Veterinary Hospital</p>
      <p class="contact__address">12 Wattle Grove Road<br>Greenvale, WA 6090</p>
      <ul class="contact__list">
        <li>
          <svg viewBox="0 0 24 24" aria-hidden="true"><path fill="var(--gold)" d="M6.6 10.8a15.1 15.1 0 0 0 6.6 6.6l2.2-2.2a1 1 0 0 1 1-.25 11.4 11.4 0 0 0 3.6.57 1 1 0 0 1 1 1V20a1 1 0 0 1-1 1A17 17 0 0 1 3 4a1 1 0 0 1 1-1h3.5a1 1 0 0 1 1 1c0 1.25.2 2.45.57 3.57a1 1 0 0 1-.25 1z"/></svg>
          (08) 9000 4821
        </li>
        <li>
          <svg viewBox="0 0 24 24" aria-hidden="true"><path fill="var(--gold)" d="M2 5h20v14H2z"/><path fill="none" stroke="var(--navy-deep)" stroke-width="1.8" d="M2 5l10 8 10-8"/></svg>
          reception@brookfernvet.com.au
        </li>
        <li>
          <svg viewBox="0 0 24 24" aria-hidden="true"><g fill="none" stroke="var(--gold)" stroke-width="1.6"><circle cx="12" cy="12" r="9.5"/><ellipse cx="12" cy="12" rx="4" ry="9.5"/><path d="M2.5 12h19M4 7h16M4 17h16"/></g></svg>
          www.brookfernvet.com.au
        </li>
      </ul>
    </div>
    <div class="back-rule"></div>
    <p class="back-tagline">Life Long Companions, Lifelong Care</p>
    <div class="brand">
      <span class="brand__dot"></span>
      <p class="brand__name"><span class="main">Brookfern</span><span class="sub">Veterinary Hospital</span></p>
    </div>
  </section>

</main>
</body>
</html>
```